label design peanut butter jar to be marketed internationally for a singapore based company

We need design of 2 labels creamy peanut butter and crunch peanut butter
The design is the same only photo of product
And wording change
The logo norvale remains the same and has to be used logo of peanut has to be used
Some idea designs by our in house designer
Enclosed .
Plus a design of a competitor silver orchard

Target Market(s)

international specially emerging markets

Industry/Entity Type

It Company

Requirements
Must have
• norvale logo
• peanut logo

```html
<!DOCTYPE html>
<html lang="en">
<head>
<meta charset="utf-8">
<title>Norvale Creamy Peanut Butter Label</title>
<link rel="stylesheet" href="https://fonts.googleapis.com/css2?family=Roboto+Slab:wght@900&family=Archivo:wght@700;800&display=swap">
<style>
  :root {
    --page: #eeeeee;
    --purple-deep: #3d1570;
    --purple: #5a2a92;
    --orange: #f28a1c;
    --orange-light: #ffc24a;
    --orange-dark: #d9661c;
    --yellow: #ffe330;
    --gold: #f5c400;
    --red: #c8171d;
    --white: #ffffff;
    --peanut: #c98a45;
    --peanut-light: #e2b27a;
    --peanut-dark: #9a6430;
  }
  * { margin: 0; padding: 0; box-sizing: border-box; }
  html, body {
    width: 800px; height: 1200px; overflow: hidden;
    background: var(--page);
  }
  .canvas {
    position: relative; width: 800px; height: 1200px;
    display: flex; align-items: center; justify-content: center;
  }
  .label {
    position: relative; width: 720px; height: 1040px; overflow: hidden;
    background: radial-gradient(circle at 50% 50%, var(--orange-light) 0%, var(--orange) 30%, var(--orange-dark) 46%, var(--purple) 64%, var(--purple-deep) 100%);
  }
  .label__arcs { position: absolute; inset: 0; width: 100%; height: 100%; }
  .brand {
    position: absolute; top: 190px; left: 0; right: 0;
    display: flex; flex-direction: column; align-items: center; gap: 8px;
  }
  .brand__row { display: flex; align-items: center; gap: 18px; }
  .brand__dot { width: 28px; height: 28px; border-radius: 50%; background: var(--white); }
  .brand__name {
    font-family: "Archivo", Arial, sans-serif; font-weight: 800;
    font-size: 92px; letter-spacing: 6px; color: var(--white); line-height: 1;
  }
  .brand__tag {
    font-family: "Archivo", Arial, sans-serif; font-weight: 700;
    font-size: 22px; letter-spacing: 4px; color: var(--white);
  }
  .product-photo {
    position: absolute; top: 360px; left: 90px; width: 540px; height: 330px;
    border-radius: 24px;
    background: radial-gradient(ellipse at 50% 45%, var(--peanut-light) 0%, var(--peanut) 60%, var(--peanut-dark) 100%);
  }
  .banner {
    position: absolute; top: 730px; left: 130px; width: 460px; height: 130px;
    border-radius: 26px; background: var(--yellow);
    border: 6px solid var(--gold);
    display: flex; flex-direction: column; align-items: center; justify-content: center;
  }
  .banner__line {
    font-family: "Roboto Slab", Georgia, serif; font-weight: 900;
    font-size: 40px; line-height: 1.1; color: var(--red); text-transform: uppercase;
    white-space: nowrap;
  }
  .net-weight {
    position: absolute; top: 885px; left: 0; right: 0; text-align: center;
    font-family: "Archivo", Arial, sans-serif; font-weight: 700;
    font-size: 28px; letter-spacing: 3px; color: var(--white);
  }
</style>
</head>
<body>
<main class="canvas">
  <section class="label">
    <svg class="label__arcs" viewBox="0 0 720 1040" aria-hidden="true">
      <path d="M40 160 Q360 40 680 160" fill="none" stroke="var(--yellow)" stroke-width="8"/>
      <path d="M40 950 Q360 1050 680 950" fill="none" stroke="var(--yellow)" stroke-width="8"/>
    </svg>

    <div class="brand">
      <div class="brand__row">
        <span class="brand__dot"></span>
        <span class="brand__name">NORVALE</span>
      </div>
      <span class="brand__tag">QUALITY</span>
    </div>

    <div class="product-photo" role="img" aria-label="Product photo: a steel spoon heaped with swirled creamy peanut butter"></div>

    <div class="banner">
      <span class="banner__line">Creamy</span>
      <span class="banner__line">Peanut Butter</span>
    </div>

    <p class="net-weight">200 GRAMS</p>
  </section>
</main>
</body>
</html>
```